Sonavera 4x6 direct mail postcard

We are looking to "refresh" some of our collateral, including our 4x6 postcard template. I am attaching 3 samples of postcards we have used in the past for your reference.

I am also attaching our brand guidelines with font and color palette as well as literature and advertising layout examples. We don't need to stick with the examples provided so feel free to be creative.

Target Market(s)

Individual consumers with potential or established hearing loss, or influencers who may have a friend/family member with hearing loss

Industry/Entity Type

Health Care

Font styles to use
Other font styles liked:
• Value and Univers (fonts (attached)

Requirements
Must have
• Please use brand guidelines for correct colors and fonts
• Please use logos provided
• Please use content shown in the samples provided
• The featured offer/benefit detail and call-to-action (phone number and/or website) should be the focal point of the piece.
Nice to have
• Use less of the primary red color and incorporate some of the other colors/textures from the attached guidelines, literature and advertising reference decks attached.

```html
<!DOCTYPE html>
<html lang="en">
<head>
<meta charset="utf-8">
<title>Sonavera 4x6 Postcard</title>
<link href="https://fonts.googleapis.com/css2?family=Fredoka:wght@500;600&family=Parisienne&family=Roboto:wght@400;500;700&display=swap" rel="stylesheet">
<style>
:root{
  --bg:#6b6b6b;
  --red:#d9263a;
  --red-deep:#c8173f;
  --orange:#ea6a26;
  --orange-light:#f0902a;
  --yellow:#ffd21f;
  --peach:#f6cfb9;
  --purple:#5b2a8f;
  --magenta:#c4124f;
  --white:#ffffff;
  --ink:#222222;
}
*{margin:0;padding:0;box-sizing:border-box}
html,body{width:1200px;height:974px;overflow:hidden;background:var(--bg)}
.stage{position:relative;width:1200px;height:974px}
.card{position:absolute;top:298px;width:642px;height:428px;transform:scale(.88);transform-origin:0 0;overflow:hidden;box-shadow:0 6px 18px rgba(0,0,0,.35);font-family:"Roboto",Arial,sans-serif}
.card--front{left:20px}
.card--back{left:615px;background:var(--white)}
.card svg.bg{position:absolute;inset:0}
.abs{position:absolute}

/* front */
.front-title{left:22px;top:52px;font-family:"Fredoka",sans-serif;font-weight:600;font-size:38px;color:var(--yellow);letter-spacing:.3px}
.front-script{left:38px;top:96px;font-family:"Parisienne",cursive;font-size:62px;color:var(--white);letter-spacing:3px}
.brand-name{left:40px;top:276px;font-family:"Roboto",Arial,sans-serif;font-weight:500;font-size:34px;line-height:40px;color:var(--white)}
.brand-sub{left:40px;top:320px;font-family:"Roboto",Arial,sans-serif;font-weight:500;font-size:14px;line-height:16px;color:var(--white)}
.client-logo{left:60px;top:372px;font-size:14px;color:var(--white)}

/* back */
.back-title{left:18px;top:10px;font-family:"Fredoka",sans-serif;font-weight:600;font-size:34px;color:var(--orange-light);letter-spacing:.5px}
.back-title span{color:var(--red)}
.back-sub{left:20px;top:47px;font-size:20px;color:var(--orange)}
.intro{left:17px;top:85px;width:330px;font-size:12.5px;line-height:14.5px;color:var(--white)}
.offer-head{left:17px;top:132px;font-size:11px;font-weight:700;color:var(--purple)}
.offer-list{left:17px;top:146px;list-style:none;font-size:9.3px;line-height:13px;color:var(--white)}
.offer-list b{color:var(--purple);font-weight:500}
.offer-list li::before{content:"\2713";color:var(--purple);margin-right:6px}
.pill{left:55px;top:198px;width:242px;height:20px;border-radius:10px;background:var(--purple);color:var(--white);font-size:13px;font-weight:500;text-align:center;line-height:20px}
.ribbon-text{color:var(--white);text-align:center;width:90px}
.ribbon-text strong{font-size:17px}
.ribbon-text small{display:block;font-size:8px;margin-top:-2px}
.or-box{left:164px;top:240px;width:28px;height:14px;background:var(--orange);color:var(--peach);font-size:12px;text-align:center;line-height:13px}
.expires{left:0;width:364px;top:283px;text-align:center;font-size:15px;color:var(--ink)}
.fine-note{left:0;width:364px;top:304px;text-align:center;font-size:5.5px;color:var(--ink)}
.call{left:18px;top:320px;font-size:15px;font-weight:500;line-height:17px;color:var(--white)}
.disclaimer{left:18px;top:359px;width:335px;font-size:5.6px;line-height:7px;color:var(--white)}
.footer-note{left:18px;top:408px;font-size:5.6px;color:var(--white)}
.stamp{left:533px;top:44px;width:72px;height:72px;border:1px solid var(--ink)}
.address-line{left:435px;width:170px;height:1px;background:var(--ink)}
</style>
</head>
<body>
<div class="stage">

  <section class="card card--front">
    <svg class="bg" width="642" height="428" viewBox="0 0 642 428">
      <defs>
        <linearGradient id="frontGrad" x1="0" y1="0" x2="1" y2="0.3">
          <stop offset="0" stop-color="#d9263a"/>
          <stop offset="1" stop-color="#ec6a22"/>
        </linearGradient>
        <linearGradient id="photoGrad" x1="0" y1="0" x2="0" y2="1">
          <stop offset="0" stop-color="#ece8ec"/>
          <stop offset=".35" stop-color="#b9aea8"/>
          <stop offset="1" stop-color="#6e5f55"/>
        </linearGradient>
      </defs>
      <rect width="642" height="428" fill="url(#frontGrad)"/>
      <polygon points="372,0 392,0 350,85" fill="var(--purple)"/>
      <polygon points="392,0 642,0 642,428 545,428 315,155" fill="url(#photoGrad)" role="img" aria-label="Photo of a family walking outdoors on a hillside path"/>
      <polygon points="415,428 545,428 470,340" fill="var(--magenta)"/>
    </svg>
    <div class="abs front-title">Hearing Health</div>
    <div class="abs front-script">for life</div>
    <div class="abs brand-name">Sonavera</div>
    <div class="abs brand-sub">Hearing Health Care</div>
    <div class="abs client-logo">&lt;CLIENT LOGO HERE&gt;</div>
  </section>

  <section class="card card--back">
    <svg class="bg" width="642" height="428" viewBox="0 0 642 428">
      <defs>
        <linearGradient id="bandOrange" x1="0" y1="0" x2="1" y2="0">
          <stop offset="0" stop-color="#ec8a2c"/>
          <stop offset="1" stop-color="#e85a2c"/>
        </linearGradient>
        <linearGradient id="bandRed" x1="0" y1="0" x2="1" y2="0">
          <stop offset="0" stop-color="#d9263a"/>
          <stop offset="1" stop-color="#c8173f"/>
        </linearGradient>
      </defs>
      <rect x="0" y="78" width="364" height="113" fill="url(#bandOrange)"/>
      <rect x="0" y="191" width="364" height="122" fill="var(--peach)"/>
      <rect x="0" y="313" width="364" height="115" fill="url(#bandRed)"/>
      <polygon points="64,226 160,226 155,262 114,264 110,270 68,262" fill="var(--red-deep)"/>
      <polygon points="200,226 296,226 292,262 250,264 246,270 204,262" fill="var(--red-deep)"/>
    </svg>

    <div class="abs back-title">Don’t <span>miss out</span></div>
    <div class="abs back-sub">on the sounds of life!</div>
    <p class="abs intro">Our goal is to help you find the right hearing solution by providing personalized service, high-quality care and exceptional products.</p>
    <div class="abs offer-head">We offer:</div>
    <ul class="abs offer-list">
      <li><b>Low-price guarantee*</b> - find a lower price locally, and we beat it by 5%</li>
      <li><b>60-day risk-free trial</b> - 100% money back guarantee if not completely satisfied</li>
      <li><b>Aftercare program</b> - 1 year follow-up care, 2 years batteries, 3 year warranty</li>
    </ul>
    <div class="abs pill">Additional* money-saving offer!</div>
    <div class="abs ribbon-text" style="left:67px;top:230px"><strong>$50</strong> off<small>one hearing aid *</small></div>
    <div class="abs or-box">or</div>
    <div class="abs ribbon-text" style="left:203px;top:230px"><strong>$125</strong> off<small>two hearing aids *</small></div>
    <div class="abs expires">Offer expires xx/xx/xxxx</div>
    <div class="abs fine-note">*Savings on top of our already discounted pricing. Please bring this offer with you to your appointment.</div>
    <div class="abs call">Call 1-800-SAMPLE<br>or visit www.sonaverausa.com/SAMPLE</div>
    <p class="abs disclaimer">*Sonavera will match a competitor's advertised price for hearing aids and bundled packages where the advertised hearing aid is offered through the Sonavera program. Price match applies to the exact manufacturer make and model and similar bundled package. Copy of a current, valid advertisement must be provided. Please call for additional details.</p>
    <div class="abs footer-note">©2017 Sonavera Hearing Health Care, Corp. | 3165DMPM/SAMPLE</div>

    <div class="abs stamp"></div>
    <div class="abs address-line" style="top:210px"></div>
    <div class="abs address-line" style="top:236px"></div>
    <div class="abs address-line" style="top:262px"></div>
    <div class="abs address-line" style="top:288px"></div>
  </section>

</div>
</body>
</html>
```